Stationery Design Project

Would like to have the design elements we created in for our website (www.brook-estates.com), incorporated in a stationery design layout.
Updates
Colors used in the logo attachments do not need to be used. We are open to different color variations. Looking for a crisp, clean, modern update using the design elements in attachments and which can also be viewed on or website.
A note to designers:
Project Deadline Extended
Reason: Due to update in our project description and requirements, we have decided to extend the deadline of this project to provide ample opportunity to all designers participating .
Requirements
Must have
- Must have continuity with the theme and design features used in our website. Have attached .jpg images of some of the design elements.

```html
<!DOCTYPE html>
<html lang="en">
<head>
<meta charset="utf-8">
<title>Brook Estates Inc. — Letterhead</title>
<link href="https://fonts.googleapis.com/css2?family=Open+Sans:wght@400;700&family=Source+Sans+3:wght@400&display=swap" rel="stylesheet">
<style>
  :root {
    --paper: #ffffff;
    --ink: #1a1a1a;
    --brand-grey: #4a4a4a;
    --rule: #8c8c8c;
    --footer-green: #2f7a3a;
  }
  html, body {
    margin: 0;
    padding: 0;
    overflow: hidden;
    background: var(--paper);
  }
  .letterhead {
    position: relative;
    width: 939px;
    height: 1200px;
    background: var(--paper);
    overflow: hidden;
    font-family: "Open Sans", Arial, sans-serif;
    color: var(--ink);
  }
  .brand-name {
    position: absolute;
    top: 78px;
    left: 0;
    width: 939px;
    margin: 0;
    text-align: center;
    font-family: "Source Sans 3", "Open Sans", sans-serif;
    font-weight: 400;
    font-size: 46px;
    letter-spacing: 0.3px;
    color: var(--brand-grey);
  }
  .rule {
    position: absolute;
    left: 48px;
    width: 836px;
    height: 2px;
    background: var(--rule);
  }
  .rule--top { top: 148px; }
  .rule--bottom { top: 1116px; }
  .letter {
    position: absolute;
    top: 262px;
    left: 71px;
    width: 799px;
    font-size: 13.4px;
    line-height: 19px;
  }
  .salutation { margin: 0 0 42px; }
  .letter-body p {
    margin: 0 0 19px;
    text-indent: 53px;
    text-align: justify;
  }
  .closing {
    position: absolute;
    top: 906px;
    left: 593px;
    margin: 0;
    font-size: 13.4px;
    line-height: 20px;
  }
  .footer-contact {
    position: absolute;
    top: 1129px;
    left: 0;
    width: 939px;
    margin: 0;
    text-align: center;
    font-size: 11.6px;
    font-weight: 700;
    color: var(--footer-green);
    word-spacing: 1px;
  }
  .footer-contact span { margin: 0 9px; }
</style>
</head>
<body>
<main class="letterhead">
  <h1 class="brand-name">Brook Estates Inc.</h1>
  <div class="rule rule--top"></div>

  <section class="letter">
    <p class="salutation">Dear To Whome This May Interest,</p>
    <div class="letter-body">
      <p>Lorem ipsum dolor sit amet, consectetuer adipiscing elit. Nullam ornare dictum ligula. Maecenas elementum suscipit nisl. Cras imperdiet leo ac felis dictum luctus. Pellentesque odio nisi, accumsan nec, scelerisque sed, consectetuer nec, justo. Sed tortor sapien, suscipit id, pulvinar vel, elementum id, lorem. Nullam consectetuer risus sit amet nibh. Vestibulum consectetuer, quam vitae euismod volutpat, magna magna consectetuer dui, et accumsan magna dui non nibh. Morbi adipiscing consequat erat. Vivamus quis massa eget orci fermentum laoreet. Morbi posuere purus. Duis feugiat lacus vel nisi. Aliquam ipsum felis, pretium sed, vehicula vel, dictum eget, nibh. Morbi turpis nulla, luctus viverra, pretium in, suscipit vitae, purus.</p>
      <p>Morbi gravida lacus sed lorem. Mauris vestibulum. Cras vehicula porta eros. Curabitur ut justo vel pede elementum semper. Integer pretium pulvinar augue. Aenean ut nisl non lectus porta feugiat. Mauris iaculis pede a risus. Suspendisse mollis. Donec suscipit. Sed tellus magna, tempus a, ultricies in, dignissim et, nulla. Pellentesque habitant morbi tristique senectus et netus et malesuada fames ac turpis egestas. Suspendisse potenti. Proin viverra vulputate pede. Sed nec mauris ut turpis convallis tempus. Maecenas id justo vitae lacus fringilla interdum. Nulla diam.</p>
      <p>Phasellus interdum dictum tellus. Donec convallis leo in orci. Vestibulum eget nibh. Nullam consectetuer blandit elit. Cras non ipsum ut nulla pulvinar consequat. Maecenas tincidunt, dui sed interdum vehicula, justo arcu tempus risus, id semper arcu velit sit amet mi. Donec sem. Sed pulvinar fringilla elit. Quisque ante. Cras tempor lobortis velit. Phasellus porta arcu sit amet libero. Aenean aliquet, leo in porta aliquam, est tortor accumsan justo, vel ultrices leo dui nec velit. Etiam vel nibh. Quisque eu ante ut diam auctor molestie. Nullam mattis, nulla et molestie cursus, neque orci consectetuer nisl, eget consequat sapien pede vitae augue. Fusce pretium velit et lacus. Cras commodo sagittis velit. Proin lobortis, diam in semper viverra, enim pede adipiscing massa, a convallis enim sem consectetuer odio.</p>
    </div>
  </section>

  <p class="closing">Sincerely,<br>Brook Estates</p>

  <div class="rule rule--bottom"></div>
  <p class="footer-contact">
    <span>418 Alder Lane Suite 102 Dayton, GA 30512</span><span>PHONE: (706) 555-0142</span><span>FAX: (706) 555-0178</span><span>www.brook-estates.com</span>
  </p>
</main>
</body>
</html>
```